Great looking banner designs for our website www.stoutwellcases.com

Our website is a key marketing platform and the banners need some work. We need 4-5 great looking banner designs.
StoutWell cases are the toughest around and have a unique accessory attachment system and range of accessories. We like to see banners that show our products, how they can be used and with key selling messages

Target Market(s)

Key markets are construction and outdoor workers, fishing and boating, cycling, camping and other adventure activities.

Industry/Entity Type

Marketing

Font styles to use
Other font styles liked:
• Homenaje

Requirements
Must have
• Ideally we'd like the banners to give customers a good idea of the capabilities of our products and the situations they can be used.

This is a dropbox link to a range of images and renders that can be used for the banners.
https://www.parcelnest.com/sh/k7p2qx9ma3tz118/Tq4vLmw8nE

We are also happy to look at increasing the banner size on the home page.

Banners should show the Zelvar case range + different accessories.
We have our new Stoutwell outdoor Bluetooth speaker arriving soon so need an appropriate banner
Banner size should be 1270 x 520

```html
<!DOCTYPE html>
<html lang="en">
<head>
<meta charset="utf-8">
<title>StoutWell Cases – Website Banners</title>
<link rel="stylesheet" href="https://fonts.googleapis.com/css2?family=Open+Sans:wght@300;400&display=swap">
<style>
  :root {
    --page: #ffffff;
    --banner-black: #0e0e0e;
    --swoosh-light: #4d4d4d;
    --swoosh-dark: #151515;
    --stripe: #000000;
    --silver: #c9c9c9;
    --type-white: #ffffff;
    --accent-orange: #f07a3a;
    --accent-pink: #e6338f;
    --band: #2c2c2c;
  }
  * { margin: 0; padding: 0; box-sizing: border-box; }
  html, body {
    width: 1200px;
    height: 970px;
    overflow: hidden;
    background: var(--page);
  }
  .canvas {
    position: relative;
    width: 1200px;
    height: 970px;
  }
  .banner {
    position: absolute;
    left: 40px;
    width: 1113px;
    display: block;
  }
  .banner--work { top: 25px; height: 455px; }
  .banner--water { top: 497px; height: 453px; }
  .banner__base { fill: var(--banner-black); }
  .banner__stripe { fill: none; stroke: var(--stripe); stroke-width: 5; }
  .banner__rule { fill: none; stroke: var(--silver); stroke-width: 3; }
  .tagline {
    font-family: "Open Sans", sans-serif;
    font-weight: 300;
    font-size: 45px;
    fill: var(--type-white);
  }
  .tagline--work { fill: var(--accent-orange); }
  .tagline--water { fill: var(--accent-pink); }
</style>
</head>
<body>
<main class="canvas">

  <!-- Banner: work use -->
  <svg class="banner banner--work" viewBox="0 0 1113 455" xmlns="http://www.w3.org/2000/svg">
    <defs>
      <linearGradient id="swooshWork" x1="0" y1="0" x2="1" y2="0">
        <stop offset="0" stop-color="var(--swoosh-dark)"/>
        <stop offset="0.42" stop-color="var(--swoosh-dark)"/>
        <stop offset="0.68" stop-color="var(--swoosh-light)"/>
        <stop offset="0.7" stop-color="var(--stripe)"/>
        <stop offset="1" stop-color="var(--stripe)"/>
      </linearGradient>
      <linearGradient id="skyPhoto" x1="0" y1="0" x2="0" y2="1">
        <stop offset="0" stop-color="#8fa9c4"/>
        <stop offset="0.6" stop-color="#d9e2ec"/>
        <stop offset="1" stop-color="#b7c3cf"/>
      </linearGradient>
      <linearGradient id="bandWork" x1="0" y1="0" x2="1" y2="0">
        <stop offset="0" stop-color="var(--band)"/>
        <stop offset="1" stop-color="var(--band)" stop-opacity="0.2"/>
      </linearGradient>
      <linearGradient id="casesWork" x1="0" y1="0" x2="1" y2="0">
        <stop offset="0" stop-color="#f07a3a"/>
        <stop offset="0.3" stop-color="#4a4a4a"/>
        <stop offset="0.7" stop-color="#3a3a3a"/>
        <stop offset="1" stop-color="#d9338a"/>
      </linearGradient>
      <clipPath id="belowCurveWork">
        <path d="M0 96 C250 140 520 205 690 176 C820 150 980 120 1113 128 V455 H0 Z"/>
      </clipPath>
    </defs>
    <rect class="banner__base" width="1113" height="455"/>
    <path d="M0 0 H1113 V128 C980 120 820 150 690 176 C520 205 250 140 0 96 Z" fill="url(#swooshWork)"/>
    <path class="banner__stripe" d="M0 40 C250 80 500 130 690 140 C820 146 980 118 1113 98"/>
    <path class="banner__stripe" d="M0 58 C250 98 500 148 690 156 C820 160 980 130 1113 110"/>
    <rect role="img" aria-label="Photo: pilot in white shirt checking an orange StoutWell case beside a helicopter under open sky"
          x="432" y="110" width="681" height="345" fill="url(#skyPhoto)" clip-path="url(#belowCurveWork)"/>
    <path class="banner__rule" d="M0 96 C250 140 520 205 690 176 C820 150 980 120 1113 128"/>
    <rect role="img" aria-label="Product shot: four StoutWell cases in orange, black, grey and pink"
          x="861" y="19" width="187" height="95" rx="8" fill="url(#casesWork)"/>
    <rect x="0" y="366" width="432" height="65" fill="url(#bandWork)"/>
    <text class="tagline" x="12" y="279">DURABLE.</text>
    <text class="tagline" x="12" y="346">CONVENIENT.</text>
    <text class="tagline tagline--work" x="12" y="413">WORKPROOF.</text>
  </svg>

  <!-- Banner: water use -->
  <svg class="banner banner--water" viewBox="0 0 1113 453" xmlns="http://www.w3.org/2000/svg">
    <defs>
      <linearGradient id="swooshWater" x1="1" y1="0" x2="0" y2="0">
        <stop offset="0" stop-color="var(--swoosh-dark)"/>
        <stop offset="0.42" stop-color="var(--swoosh-dark)"/>
        <stop offset="0.68" stop-color="var(--swoosh-light)"/>
        <stop offset="0.7" stop-color="var(--stripe)"/>
        <stop offset="1" stop-color="var(--stripe)"/>
      </linearGradient>
      <linearGradient id="riverPhoto" x1="0" y1="0" x2="1" y2="1">
        <stop offset="0" stop-color="#7d8a66"/>
        <stop offset="0.45" stop-color="#5d6b4c"/>
        <stop offset="0.7" stop-color="#c8577f"/>
        <stop offset="1" stop-color="#c9bfb2"/>
      </linearGradient>
      <linearGradient id="bandWater" x1="1" y1="0" x2="0" y2="0">
        <stop offset="0" stop-color="var(--band)"/>
        <stop offset="1" stop-color="var(--band)" stop-opacity="0.2"/>
      </linearGradient>
      <linearGradient id="casesWater" x1="0" y1="0" x2="1" y2="0">
        <stop offset="0" stop-color="#d9338a"/>
        <stop offset="0.3" stop-color="#3a3a3a"/>
        <stop offset="0.7" stop-color="#4a4a4a"/>
        <stop offset="1" stop-color="#f07a3a"/>
      </linearGradient>
      <clipPath id="belowCurveWater">
        <path d="M1113 96 C863 140 593 205 423 176 C293 150 133 120 0 128 V453 H1113 Z"/>
      </clipPath>
    </defs>
    <rect class="banner__base" width="1113" height="453"/>
    <path d="M1113 0 H0 V128 C133 120 293 150 423 176 C593 205 863 140 1113 96 Z" fill="url(#swooshWater)"/>
    <path class="banner__stripe" d="M1113 40 C863 80 613 130 423 140 C293 146 133 118 0 98"/>
    <path class="banner__stripe" d="M1113 58 C863 98 613 148 423 156 C293 160 133 130 0 110"/>
    <rect role="img" aria-label="Photo: hands filming a river kayak scene with a phone in a pink StoutWell case"
          x="0" y="110" width="666" height="343" fill="url(#riverPhoto)" clip-path="url(#belowCurveWater)"/>
    <path class="banner__rule" d="M1113 96 C863 140 593 205 423 176 C293 150 133 120 0 128"/>
    <rect role="img" aria-label="Product shot: four StoutWell cases in pink, black, grey and orange"
          x="66" y="15" width="184" height="90" rx="8" fill="url(#casesWater)"/>
    <rect x="666" y="362" width="447" height="64" fill="url(#bandWater)"/>
    <text class="tagline" x="1104" y="273" text-anchor="end">DURABLE.</text>
    <text class="tagline" x="1104" y="340" text-anchor="end">ATTRACTIVE.</text>
    <text class="tagline tagline--water" x="1104" y="409" text-anchor="end">WATERPROOF.</text>
  </svg>

</main>
</body>
</html>
```